Progressive Flow Chart

Looking for a progressive flow chart centered and branching off. They all build on each other 1-3. There will be 3 different pages.

Target Market(s)

Business Owners - High Net worth Individuals

Industry/Entity Type

Finance & Business Consulting

Font styles to use
Serif

Colors
0054AA
0677BA
7BADD7
CADEEF
E8F1F8
0094D4
00A9DD
6FCCEA
C7EBF8
E9F6FB
00AB8E
00BBA5
67D7C9
C6EFE9
E9F9F6

Requirements
Nice to have
• Clean, simple, and approachable.
Should not have
• Very Busy

```html
<!DOCTYPE html>
<html lang="en">
<head>
<meta charset="utf-8">
<title>Progressive Flow Chart</title>
<link rel="stylesheet" href="https://fonts.googleapis.com/css2?family=Montserrat:wght@300;400;500;600;700&display=swap">
<style>
  :root {
    --navy: #161c3c;
    --canvas: #e5e7e9;
    --card: #ffffff;
    --ink: #222733;
    --line: #2f333b;
    --tier1: #2ee0b0;
    --tier2: #2f3f88;
    --tier3: #7badd7;
    --arrow-navy: #33439a;
    --arrow-green: #2fe0a8;
    --brand: #2fd0c0;
    --circle-a: #1c9be3;
    --circle-b: #30e6b0;
  }
  * { margin: 0; padding: 0; box-sizing: border-box; }
  html, body { width: 1200px; height: 849px; overflow: hidden; }
  body {
    position: relative;
    background: var(--canvas);
    font-family: "Montserrat", Arial, sans-serif;
    color: var(--ink);
  }
  .masthead {
    position: absolute; left: 0; top: 0;
    width: 1200px; height: 159px;
    background: var(--navy);
  }
  .masthead__title {
    position: absolute; left: 100px; top: 44px;
    color: #fff; font-size: 33px; line-height: 42px; letter-spacing: 0.5px;
  }
  .masthead__title span { display: block; }
  .masthead__title .light { font-weight: 300; }
  .masthead__title .bold { font-weight: 700; }
  .brand {
    position: absolute; left: 1030px; top: 34px; width: 120px;
    display: flex; flex-direction: column; align-items: center; gap: 10px;
  }
  .brand__dot {
    width: 52px; height: 52px; border-radius: 50%;
    border: 4px solid var(--brand);
  }
  .brand__name {
    color: var(--brand); font-weight: 500; font-size: 15px; letter-spacing: 2px;
    white-space: nowrap;
  }
  .chart-lines, .tier-badges { position: absolute; left: 0; top: 0; }
  .tier-badges { pointer-events: none; }
  .tier-badges text, .chart-lines .badge-num {
    font-family: "Montserrat", Arial, sans-serif; font-weight: 600; font-size: 17px; fill: #fff;
  }
  .chart-label {
    position: absolute; font-size: 14px; line-height: 17px; color: var(--ink); white-space: nowrap;
  }
  .card {
    position: absolute; width: 180px; height: 110px;
    background: var(--card); border-radius: 6px;
    box-shadow: 0 3px 8px rgba(20, 30, 60, 0.10);
    display: flex; flex-direction: column; align-items: center; justify-content: center;
    text-align: center; padding-bottom: 8px;
  }
  .card::after {
    content: ""; position: absolute; left: 0; right: 0; bottom: 0; height: 7px;
    border-radius: 0 0 6px 6px; background: var(--bar);
  }
  .card--tier1 { --bar: var(--tier1); }
  .card--tier2 { --bar: var(--tier2); }
  .card--tier3 { --bar: var(--tier3); }
  .card__title { font-weight: 600; font-size: 17px; line-height: 20px; letter-spacing: 0.3px; }
  .card__note { font-size: 12.5px; line-height: 16px; margin-top: 7px; }
</style>
</head>
<body>
  <header class="masthead">
    <h1 class="masthead__title"><span class="light">PROGRESSIVE</span><span class="bold">FLOW CHART</span></h1>
    <div class="brand"><div class="brand__dot"></div><div class="brand__name">NVS WEALTH</div></div>
  </header>

  <svg class="chart-lines" width="1200" height="849" viewBox="0 0 1200 849" aria-hidden="true">
    <defs>
      <linearGradient id="trustFill" x1="0" y1="0" x2="1" y2="0.3">
        <stop offset="0" stop-color="#1c9be3"/>
        <stop offset="1" stop-color="#30e6b0"/>
      </linearGradient>
      <path id="trustArc" d="M513 468 A98 98 0 0 1 709 468"/>
    </defs>
    <g stroke="var(--line)" stroke-width="1.6" fill="none">
      <line x1="387" y1="469" x2="524" y2="469"/>
      <line x1="268" y1="524" x2="268" y2="690"/>
      <line x1="327" y1="524" x2="327" y2="690"/>
      <line x1="387" y1="512" x2="582" y2="690"/>
      <line x1="327" y1="690" x2="515" y2="544"/>
      <line x1="632" y1="590" x2="632" y2="690"/>
      <line x1="712" y1="532" x2="893" y2="690"/>
      <line x1="733" y1="494" x2="953" y2="690"/>
    </g>
    <polygon points="446,469 426,460 431,469 426,478" fill="var(--arrow-navy)"/>
    <polygon points="268,592 259,612 268,607 277,612" fill="var(--arrow-green)"/>
    <polygon points="327,620 318,600 327,605 336,600" fill="var(--arrow-navy)"/>
    <polygon points="505,620 484.1,613.2 493.9,609.9 496.3,599.8" fill="var(--arrow-navy)"/>
    <polygon points="412,624 401.7,643.4 400.2,633.2 390.7,629.2" fill="var(--arrow-green)"/>
    <polygon points="632,636 623,616 632,621 641,616" fill="var(--arrow-green)"/>

    <circle cx="610" cy="462" r="127" fill="#fff"/>
    <circle cx="610" cy="462" r="84" fill="url(#trustFill)"/>
    <text font-family="Montserrat, Arial, sans-serif" font-weight="500" font-size="15" fill="#222733" letter-spacing="1.5">
      <textPath href="#trustArc" startOffset="50%" text-anchor="middle">LIVING TRUST</textPath>
    </text>
    <text x="610" y="456" text-anchor="middle" font-family="Montserrat, Arial, sans-serif" font-weight="500" font-size="21" fill="#fff">YOU</text>
    <text x="610" y="484" text-anchor="middle" font-family="Montserrat, Arial, sans-serif" font-weight="500" font-size="21" fill="#fff">TRUSTEE</text>
    <g transform="translate(494 373)">
      <path d="M2 7 Q28 -3 54 7 L31 34 Q28 37 25 34 Z" fill="var(--tier1)" stroke="#fff" stroke-width="2" stroke-linejoin="round"/>
      <text class="badge-num" x="28" y="23" text-anchor="middle">1</text>
    </g>
  </svg>

  <span class="chart-label" style="left:412px;top:486px;">Invest</span>
  <span class="chart-label" style="left:215px;top:600px;transform:rotate(-90deg);">Interest</span>
  <span class="chart-label" style="left:312px;top:596px;transform:rotate(-90deg);">Investment</span>
  <span class="chart-label" style="left:428px;top:600px;transform:rotate(-38deg);">Income</span>
  <span class="chart-label" style="left:623px;top:628px;transform:rotate(-90deg);">Income</span>
  <span class="chart-label" style="left:433px;top:734px;">Rent</span>

  <div class="card card--tier3" style="left:208px;top:208px;"><div class="card__title">CRT</div></div>
  <div class="card card--tier3" style="left:521px;top:208px;"><div class="card__title">DAF</div></div>
  <div class="card card--tier3" style="left:831px;top:208px;"><div class="card__title">GRATS' IDGT'S</div></div>

  <div class="card card--tier2" style="left:208px;top:415px;">
    <div class="card__title">BANK</div>
    <div class="card__note">Makes Investments To<br>Real Estate + Business</div>
  </div>

  <div class="card card--tier1" style="left:208px;top:690px;"><div class="card__title">REAL ESTATE<br>LLC</div></div>
  <div class="card card--tier1" style="left:521px;top:690px;">
    <div class="card__title">BUSINESS</div>
    <div class="card__note">LLC - Member/ Manager<br>Corp - President</div>
  </div>
  <div class="card card--tier2" style="left:831px;top:690px;"><div class="card__title">INSURANCE</div></div>

  <svg class="tier-badges" width="1200" height="849" viewBox="0 0 1200 849" aria-hidden="true">
    <defs>
      <path id="badgeShape" d="M2 7 Q28 -3 54 7 L31 34 Q28 37 25 34 Z" stroke="#fff" stroke-width="2" stroke-linejoin="round"/>
    </defs>
    <g transform="translate(184 296)"><use href="#badgeShape" fill="var(--tier3)"/><text x="28" y="23" text-anchor="middle">3</text></g>
    <g transform="translate(497 296)"><use href="#badgeShape" fill="var(--tier3)"/><text x="28" y="23" text-anchor="middle">3</text></g>
    <g transform="translate(807 296)"><use href="#badgeShape" fill="var(--tier3)"/><text x="28" y="23" text-anchor="middle">3</text></g>
    <g transform="translate(184 503)"><use href="#badgeShape" fill="var(--tier2)"/><text x="28" y="23" text-anchor="middle">2</text></g>
    <g transform="translate(184 778)"><use href="#badgeShape" fill="var(--tier1)"/><text x="28" y="23" text-anchor="middle">1</text></g>
    <g transform="translate(497 778)"><use href="#badgeShape" fill="var(--tier1)"/><text x="28" y="23" text-anchor="middle">1</text></g>
    <g transform="translate(807 778)"><use href="#badgeShape" fill="var(--tier2)"/><text x="28" y="23" text-anchor="middle">2</text></g>
  </svg>
</body>
</html>
```